Willowmere Counseling (Endure - Mend - Flourish) - Double Sided Business Card

I would like a 2-sided business card. Front: Matte Black or Navy with Logo & Tagline. Back: Name, Address, Phone Number, Email, & Website (maybe would like to include a small map pin-pointing location); Prefer front to be a gold/silver foil (iridescent); Back prefer white or light colored background with lettering that is easy to read and simple

Target Market(s)

Individuals & Couples (13 y.o. - ALL Adults); High end clientele

Industry/Entity Type

Licensed Professional Counselor (Mental Health)

Contact Information for Business Card

Name: Willowmere Counseling; Tagline: Endure - Mend - Flourish; Address: 3870 N. Garrick Ave., Suite 214, Fort Worth, TX 76132; Phone: (214) 555-0187; Website: www.WillowmereCounseling.example

Font styles to use
Serif

Requirements
Must have
• Logo on Front (Large) prefer gold/silver foil on a matte dark color (i.e. black, navy, etc.); Back of Card: All other relevant information

```html
<!DOCTYPE html>
<html lang="en">
<head>
<meta charset="utf-8">
<title>Willowmere Counseling – Business Card</title>
<link href="https://fonts.googleapis.com/css2?family=Cinzel:wght@500;600&family=Arimo:wght@400&display=swap" rel="stylesheet">
<style>
  :root {
    --backdrop: #d3d3d3;
    --card-light: #ffffff;
    --card-dark: #68696b;
    --gold: #d4b356;
    --foil: #d9b84a;
    --ink: #3c3c3c;
  }
  html, body {
    margin: 0;
    padding: 0;
    width: 1200px;
    height: 1200px;
    overflow: hidden;
    background: var(--backdrop);
  }
  .canvas {
    position: relative;
    width: 1200px;
    height: 1200px;
  }
  .card {
    position: absolute;
    left: 262px;
    width: 686px;
    height: 392px;
    border-radius: 18px;
    overflow: hidden;
  }
  .card--details {
    top: 165px;
    background: var(--card-light);
  }
  .card--brand {
    top: 653px;
    background: var(--card-dark);
  }
  .details {
    position: absolute;
    left: 371px;
    top: 112px;
    transform: translateX(-50%);
    text-align: center;
    font-family: "Arimo", Arial, sans-serif;
    color: var(--ink);
    font-size: 15.5px;
    line-height: 19px;
    white-space: nowrap;
  }
  .details__name {
    font-family: "Cinzel", "Times New Roman", serif;
    font-weight: 600;
    font-size: 23px;
    line-height: 26px;
    color: var(--gold);
    letter-spacing: 0.5px;
  }
  .details__role { margin-bottom: 11px; }
  .details__address { margin-bottom: 11px; }
  .brand {
    position: absolute;
    left: 0;
    right: 0;
    top: 100px;
    text-align: center;
    font-family: "Cinzel", "Times New Roman", serif;
    font-weight: 600;
    color: var(--foil);
  }
  .brand__mark {
    display: block;
    margin: 0 auto 14px;
  }
  .brand__name {
    font-size: 30px;
    letter-spacing: 1px;
    line-height: 36px;
  }
  .brand__tagline {
    font-size: 14px;
    letter-spacing: 0.8px;
    margin-top: 6px;
  }
</style>
</head>
<body>
<main class="canvas">
  <section class="card card--details" aria-label="Card back with contact details">
    <div class="details">
      <div class="details__name">Daniel Harper</div>
      <div class="details__role">President</div>
      <div class="details__address">3870 N. Garrick Ave., Suite 214<br>Fort Worth, TX 76132</div>
      <div class="details__contact">(P) (214) 555-0187<br>info@WillowmereCounseling.example<br>WillowmereCounseling.example</div>
    </div>
  </section>

  <section class="card card--brand" aria-label="Card front with name and tagline">
    <div class="brand">
      <svg class="brand__mark" width="90" height="90" viewBox="0 0 90 90" aria-hidden="true">
        <circle cx="45" cy="45" r="42" fill="var(--foil)"/>
      </svg>
      <div class="brand__name">WILLOWMERE COUNSELING</div>
      <div class="brand__tagline">ENDURE - MEND - FLOURISH</div>
    </div>
  </section>
</main>
</body>
</html>
```